Home brewer beer bottle label

I need a label for home-brew beer bottles. My sons and I all make our own beer. It should say Kessner Ale in blackletter (because we are of German heritage) (EDIT: ACTUALLY WE ARE LIKING OTHER TYPEFACE NOW) and the designer will need to work in aspects of the Kessner family (crest attached). Finally we will need two blank areas or lines for (1) what kind of beer (handwritten) and (2) who made it (the Beerista!) I have attached a rough sketch, but feel free to ignore and be creative. No color requirements. (EDIT: ACTUALLY, MY WIFE LIKES THE LITTLE BIT OF PURPLE IN THE 4TH DESIGN) Would like the logotype portion of the label to be usable on its own as a family logo. (EDIT; THIS IS LESS IMPORTANT NOW). I have attached another file sketch, which shows using the parts of the family crest w/out trying to replicate it. Thanks, everyone, for the good work....
Updates

Project Deadline Extended
Reason: Extending because my wife is out of town until Wednesday and I need her input.

Target Market(s)

Mostly friends and family at the wedding.

Industry/Entity Type

Work

Font styles to use
Serif
Sans Serif

Requirements
Must have
• Tightly kerned lettering,
Nice to have
• Color, one Group of Elements in Indesign and the print file, "Beer" and "Beerista" lines
Should not have
• Hard to see logo or logo type

```html
<!DOCTYPE html>
<html lang="en">
<head>
<meta charset="utf-8">
<title>Kessner Ale – Lager Label</title>
<link rel="stylesheet" href="https://fonts.googleapis.com/css2?family=UnifrakturMaguntia&family=Bodoni+Moda:wght@800&display=swap">
<style>
  :root {
    --backdrop: #e9e6e1;
    --label-black: #1e1e1e;
    --band-black: #262626;
    --cream: #fbf9f1;
    --cream-deep: #efe9d6;
    --gold-light: #fff1a6;
    --gold: #e0b43a;
    --gold-dark: #9a6a12;
    --ink: #1b1b1b;
  }
  * { box-sizing: border-box; margin: 0; padding: 0; }
  html, body { width: 1000px; height: 1200px; overflow: hidden; }
  body { background: var(--backdrop); position: relative; }

  .label {
    position: absolute;
    left: 133px; top: 55px;
    width: 735px; height: 1090px;
    background: var(--label-black);
    box-shadow: 0 6px 24px rgba(0,0,0,.25);
  }
  .label-shapes { position: absolute; inset: 0; }

  .brand-name {
    position: absolute;
    left: 25px; width: 685px; top: 250px;
    text-align: center;
    font-family: "Bodoni Moda", serif;
    font-weight: 800;
    font-size: 84px;
    letter-spacing: -2px;
    line-height: 1;
    color: var(--ink);
  }

  .gold-text {
    background: linear-gradient(180deg, var(--gold-light) 0%, var(--gold) 50%, var(--gold-dark) 100%);
    -webkit-background-clip: text;
    background-clip: text;
    color: transparent;
  }

  .beer-style {
    position: absolute;
    left: 0; width: 100%; top: 620px;
    text-align: center;
    font-family: "UnifrakturMaguntia", serif;
    font-size: 128px;
    line-height: 1;
  }
  .beerista {
    position: absolute;
    left: 0; width: 100%; top: 875px;
    text-align: center;
    font-family: "UnifrakturMaguntia", serif;
    font-size: 56px;
    line-height: 1;
    word-spacing: 14px;
  }

  .spec {
    position: absolute;
    font-family: "Bodoni Moda", serif;
    font-weight: 800;
    font-size: 28px;
    color: var(--ink);
    line-height: 1;
  }
  .spec-volume { left: 82px; top: 995px; }
  .spec-abv { right: 82px; top: 995px; }
  .spec-batch {
    left: 264px; width: 218px; top: 1022px;
    text-align: center;
    color: var(--cream-deep);
  }
</style>
</head>
<body>
  <div class="label">
    <svg class="label-shapes" width="735" height="1090" viewBox="0 0 735 1090">
      <defs>
        <radialGradient id="creamGlow" cx="50%" cy="40%" r="70%">
          <stop offset="0" stop-color="#ffffff"/>
          <stop offset="1" stop-color="#ece6d2"/>
        </radialGradient>
        <linearGradient id="goldLine" x1="0" x2="1">
          <stop offset="0" stop-color="#9a6a12"/>
          <stop offset=".5" stop-color="#f3d070"/>
          <stop offset="1" stop-color="#9a6a12"/>
        </linearGradient>
        <linearGradient id="wheatTone" x1="0" x2="1">
          <stop offset="0" stop-color="#c99a2e"/>
          <stop offset="1" stop-color="#f4d98a"/>
        </linearGradient>
      </defs>

      <!-- wheat ornaments -->
      <rect x="30" y="32" width="215" height="36" rx="6" fill="url(#wheatTone)" role="img" aria-label="Gold wheat ear ornament, left"/>
      <rect x="490" y="32" width="215" height="36" rx="6" fill="url(#wheatTone)" role="img" aria-label="Gold wheat ear ornament, right"/>

      <!-- arched crest panel -->
      <path d="M25,100 H230 Q260,100 260,70 V57 Q260,17 300,17 H435 Q475,17 475,57 V70 Q475,100 505,100 H710 V570 H25 Z"
            fill="url(#creamGlow)" role="img" aria-label="Cream panel with soft gold sunburst rays"/>
      <rect x="25" y="566" width="685" height="5" fill="url(#goldLine)"/>

      <!-- beer style band -->
      <rect x="25" y="571" width="685" height="279" fill="var(--band-black)"/>
      <rect x="25" y="850" width="685" height="5" fill="var(--cream-deep)"/>

      <!-- beerista strip -->
      <rect x="25" y="857" width="685" height="93" fill="var(--band-black)"/>
      <line x1="80" y1="915" x2="230" y2="915" stroke="var(--gold-dark)" stroke-width="1.5"/>
      <line x1="505" y1="915" x2="655" y2="915" stroke="var(--gold-dark)" stroke-width="1.5"/>

      <!-- details panel -->
      <rect x="25" y="955" width="685" height="108" fill="url(#creamGlow)"/>
      <path d="M264,1063 V985 A109,65 0 0 1 482,985 V1063 Z" fill="var(--label-black)"/>
    </svg>

    <div class="brand-name">Kessner Ale</div>
    <div class="beer-style gold-text">Lager</div>
    <div class="beerista gold-text">Karl Kessner</div>
    <div class="spec spec-volume">330ml</div>
    <div class="spec spec-batch">batch 1 #1</div>
    <div class="spec spec-abv">4.0%Abv</div>
  </div>
</body>
</html>
```